Venture Capital and Sales/Marketing Consultancy Business Needs a Wordpress Design

I need a new web site design to replace our current site built based on Wordpress. Existing plumvane wordpress hosting can be used. Completely new design, new content and new features can be added. This is a web site for information purposes ONLY. My company offer consulting services to start up or high growth technology companies to help them with financing (venture Capital or angel investment) and marketing/sales/product management expertise. We focus on driving growth through our access to venture capitals and business development strategies. We've helped many start up companies in the past - through my consulting business operating under my name. Now I have turned this business into an organization offering not only sales/marketing expertise but also investment support to help those start up companies.
Updates

Target Market(s)

Early Stage Technology Start-ups, Technology Companies with independent intellectual properties. Venture Capital and investment companies looking into technology investment. Companies looking into market expansions in North America and APAC especially China). Product seeking business development partners to reduce marketing and operational risk in developing North American and APAC markets. Technologies demanding Intellectual Property protection in North American and Chinese market.

Industry/Entity Type

Investment

Font styles to use
Sans Serif

Colors
ffcf3e

Requirements
Must have
• Basic features such as Newsfeeds to News page.
• Following pages are required: About Us, Projects, Partners and Contact Us
• Designer will also help with:
• Implementing the design into the current wordpress account hosted by plumvane.
• All Graphics used in the design need to be included.
Nice to have
• A proposal submission page allow submission of project proposal in PDF format only. Files submitted can be automatically forwarded to an email alias.

```html
<!DOCTYPE html>
<html lang="en">
<head>
<meta charset="utf-8">
<title>Veltaris – Venture Capital &amp; Marketing Consultancy</title>
<link href="https://fonts.googleapis.com/css2?family=Roboto:wght@300;400;500&display=swap" rel="stylesheet">
<style>
:root{
  --yellow:#ffcf3e;
  --ink:#222;
  --body:#6b6b6b;
  --panel:#f3f3f3;
  --rule:#dcdcdc;
  --footer:#666666;
  --bar:#4a4a4a;
}
*{box-sizing:border-box;margin:0;padding:0}
html,body{width:1010px;height:1200px;overflow:hidden;background:#fff;font-family:'Roboto',sans-serif;color:var(--ink)}
.page{position:relative;width:1010px;height:1200px}
.abs{position:absolute}
.header{height:72px}
.logo{left:62px;top:8px;width:114px;height:112px;background:#f4f4f4;border:1px solid #ddd;z-index:3;display:flex;align-items:flex-end;justify-content:center;padding-bottom:12px;font-weight:500;font-size:14px;color:var(--yellow);letter-spacing:.5px}
.nav{right:62px;top:24px;display:flex;gap:0;font-size:10px}
.nav a{display:block;height:31px;line-height:31px;padding:0 16px;color:#333;text-decoration:none}
.nav a.active{background:var(--yellow)}
.hero{left:0;top:72px;width:1010px;height:378px;background:linear-gradient(90deg,#e9eef1 0%,#d6dde2 35%,#c5ccd2 60%,#3a3d45 78%,#2a2d33 100%)}
.hero-title{left:63px;top:182px;width:530px;height:44px;background:var(--bar);clip-path:polygon(0 0,100% 0,97% 100%,0 100%);color:var(--yellow);font-size:19px;font-weight:300;line-height:44px;padding-left:14px}
.hero-text{left:63px;top:226px;width:520px;height:88px;background:rgba(255,255,255,.72);font-size:14px;font-weight:300;line-height:22px;padding:13px 9px;color:#222}
.dots{left:69px;top:410px;display:flex;gap:6px}
.dots span{width:9px;height:9px;background:#fff;border-radius:2px}
.dots span.on{background:var(--yellow)}
h2{font-weight:400;font-size:18px;color:#222}
p.copy{font-size:9.6px;font-weight:300;line-height:18px;color:var(--body)}
.btn{display:block;width:111px;height:33px;line-height:33px;text-align:center;background:var(--yellow);font-size:10px;color:#333}
.news{left:669px;top:488px;width:279px;height:209px;background:var(--panel);padding:16px 20px}
.news-item{padding:10px 0 8px;border-bottom:1px solid var(--rule)}
.news-item:last-child{border:0}
.news-date{font-size:11px;color:#222}
.news-text{font-size:9.6px;font-weight:300;line-height:15.5px;color:var(--body)}
.news-more{font-size:10.5px;color:#e2b020;margin-top:3px}
.divider{left:62px;top:720px;width:886px;height:1px;background:var(--rule)}
.service-img{width:258px;height:125px}
.service-title{font-size:14px;color:#f0b91e;margin:16px 0 4px}
.projects{left:669px;top:747px;width:279px;height:337px;background:var(--yellow);padding:18px 19px}
.grid{display:grid;grid-template-columns:115px 116px;column-gap:12px;row-gap:13px;margin-top:14px}
.grid div{height:80px}
.footer{left:0;top:1115px;width:1010px;height:85px;background:var(--footer);padding:23px 62px}
.footer-nav{display:flex;gap:29px;font-size:11px;color:#fff;font-weight:300}
.footer-copy{font-size:9px;color:#eee;font-weight:300;margin-top:12px}
.footer-copy span{color:var(--yellow)}
</style>
</head>
<body>
<div class="page">
  <header class="header">
    <div class="abs logo">VELTARIS</div>
    <nav class="abs nav">
      <a class="active">HOME</a><a>ABOUT US</a><a>PROJECTS</a><a>PARTNERS</a><a>CONTACT US</a>
    </nav>
  </header>

  <section class="abs hero" role="img" aria-label="Photo of smiling business people in an office"></section>
  <div class="abs hero-title">We are a Venture Capital &amp; Marketing Consultancy..</div>
  <div class="abs hero-text">We help Venture Capital and investment companies looking into technology investment. Companies looking into market expansions in North America and APAC especially China.</div>
  <div class="abs dots"><span class="on"></span><span></span><span></span><span></span></div>

  <section class="abs" style="left:62px;top:482px;width:566px">
    <h2>WELCOME TO OUR WEBSITE</h2>
    <p class="copy" style="margin-top:9px">Aliquam molestie, mi et imperdiet euismod, dui purus auctor tellus, et interdum lacus lectus et ante. Sed accumsan sollicitudin sapien, sit amet adipiscing turpis gravida ac. In congue, neque ac lobortis volutpat, libero mauris varius mi, vitae suscipit ipsum ligula vitae risus. Duis aliquam nibh a dui iaculis viverra id a velit. Vivamus egestas risus in magna varius commodo. Sed semper viverra egestas. Etiam pretium porttitor lectus, vel ornare neque porta volutpat.</p>
    <p class="copy" style="margin-top:5px">Aenean a nibh eget turpis vehicula tempus ac sed massa. Vestibulum dolor nulla, ultrices ac tincidunt sed, laoreet non est. Suspendisse lobortis turpis in odio blandit ac interdum lorem euismod. Etiam risus massa, vulputate eu pellentesque et, consectetur a neque.</p>
  </section>
  <a class="abs btn" style="left:62px;top:664px">READ MORE</a>

  <aside class="abs news">
    <h2>NEWS FEEDS</h2>
    <div class="news-item"><div class="news-date">Dec 23, 2014</div><div class="news-text">Aliquam molestie, mi et imperdiet euismod, dui purus auctor tellus, et interdum lacus lectus et ante....</div><div class="news-more">Read More</div></div>
    <div class="news-item"><div class="news-date">Dec 23, 2014</div><div class="news-text">Aliquam molestie, mi et imperdiet euismod, dui purus auctor tellus, et interdum lacus lectus et ante....</div><div class="news-more">Read More</div></div>
  </aside>

  <div class="abs divider"></div>

  <section class="abs" style="left:62px;top:744px;width:560px">
    <h2>OUR SERVICES</h2>
    <p class="copy" style="margin-top:8px">Aliquam molestie, mi et imperdiet euismod, dui purus auctor tellus, et interdum lacus lectus et ante. Sed accumsan sollicitudin sapien, sit amet adipiscing turpis gravida ac.</p>
  </section>

  <article class="abs" style="left:62px;top:822px;width:258px">
    <div class="service-img" role="img" aria-label="Hand holding a globe with a rising bar chart" style="background:linear-gradient(180deg,#a9c4dc,#dbe6ee)"></div>
    <div class="service-title">Venture Capital</div>
    <p class="copy">Aliquam molestie, mi et imperdiet euismod, dui purus auctor tellus, et interdum lacus lectus et ante. Sed accum-san sollicitudin sapien...</p>
  </article>
  <a class="abs btn" style="left:62px;top:1052px">READ MORE</a>

  <article class="abs" style="left:353px;top:822px;width:258px">
    <div class="service-img" role="img" aria-label="Business team meeting around a tablet" style="background:linear-gradient(90deg,#4a4f58,#9aa0a8 55%,#d8dadd)"></div>
    <div class="service-title">Marketing Consultancy</div>
    <p class="copy">Aliquam molestie, mi et imperdiet euismod, dui purus auctor tellus, et interdum lacus lectus et ante. Sed accum-san sollicitudin sapien...</p>
  </article>
  <a class="abs btn" style="left:354px;top:1052px">READ MORE</a>

  <aside class="abs projects">
    <h2>PROJECTS</h2>
    <div class="grid">
      <div role="img" aria-label="Businessman standing on a stack of coins" style="background:linear-gradient(180deg,#e6e2dc,#c9b98e)"></div>
      <div role="img" aria-label="Financial charts and calculator" style="background:linear-gradient(135deg,#f2f2f2,#a8a8a8)"></div>
      <div role="img" aria-label="Presenter at a whiteboard with a team" style="background:linear-gradient(180deg,#eceff2,#8a8f96)"></div>
      <div role="img" aria-label="Hands reviewing charts with a tablet" style="background:linear-gradient(135deg,#f4f1ee,#c7b7a8)"></div>
      <div role="img" aria-label="Team meeting around a table" style="background:linear-gradient(180deg,#d9dde3,#8c94a0)"></div>
      <div role="img" aria-label="Hands around a green seedling" style="background:radial-gradient(circle at 50% 45%,#5d8f3a,#1a1a1a 70%)"></div>
    </div>
  </aside>

  <footer class="abs footer">
    <div class="footer-nav"><span>Home</span><span>About Us</span><span>Projects</span><span>Partners</span><span>Contact Us</span></div>
    <div class="footer-copy">Copyright © 2014.<span>Company Name</span>. All Right Reserved</div>
  </footer>
</div>
</body>
</html>
```